Home Improvements Website

I would like a website that matches our business colour scheme and uses the fonts consistent without logo. (Monserrat, Chosence & Big Noddle Tiling).
We will need numerous sections: homepage, about us, services (with tiles or links to each service - building, landscaping, decking, maintenance, roofing, gutters etc) current projects (which must be easily editable by me, who is not too tech savvy) and a contacts page with enquiry form we can link to our job management service (Tradify).

```html
<!DOCTYPE html>
<html lang="en">
<head>
<meta charset="utf-8">
<title>Marrowvale Home Improvements</title>
<link href="https://fonts.googleapis.com/css2?family=Bebas+Neue&family=Montserrat:wght@400;500;600;700&display=swap" rel="stylesheet">
<style>
:root{
  --green:#1a9a3c;
  --green-dark:#137a2f;
  --lime:#7cc33a;
  --gold:#9a7b4a;
  --ink:#222;
  --text:#444;
  --field:#2b2b2b;
  --black:#0d0d0d;
  --white:#fff;
}
*{box-sizing:border-box;margin:0;padding:0}
html,body{width:1200px;height:4348px;overflow:hidden}
body{position:relative;font-family:"Montserrat",sans-serif;color:var(--text);background:var(--white)}
.abs{position:absolute}
.display{font-family:"Bebas Neue",sans-serif;font-weight:400;color:var(--ink);letter-spacing:.5px}
a{color:inherit;text-decoration:none}

/* HERO */
.hero-gold{left:0;top:0;width:1200px;height:700px;background:var(--gold);
  clip-path:polygon(0 0,100% 0,100% 580px,50% 678px,0 580px)}
.hero-photo{left:0;top:0;width:1200px;height:700px;
  background:linear-gradient(180deg,#5d9bd6 0%,#a9cdee 45%,#c79a62 72%,#8a5d33 100%);
  clip-path:polygon(0 0,100% 0,100% 568px,50% 666px,0 568px)}
.logo{left:110px;top:40px;width:126px;height:90px;display:flex;align-items:center;justify-content:center;
  font-family:"Bebas Neue",sans-serif;font-size:30px;color:var(--ink);background:var(--white);border-radius:8px;text-align:center;line-height:1}
.nav{top:38px;left:398px;display:flex;gap:34px;font-size:13px;font-weight:500;color:var(--ink);text-transform:uppercase}
.nav .active{font-weight:600}
.btn{display:flex;align-items:center;justify-content:center;font-size:13px;font-weight:500;color:var(--white);text-transform:uppercase;border-radius:3px}
.btn-lime{background:var(--lime)}
.btn-green{background:var(--green)}
.btn-gold{background:var(--gold)}
.hero-title{left:0;width:1200px;text-align:center;font-size:62px;line-height:72px}
.hero-title .hl{color:var(--lime)}
.hero-sub{left:0;width:1200px;top:310px;text-align:center;font-size:16px;line-height:26px;color:var(--ink)}
.call{top:387px;height:45px;width:144px;border:2px solid var(--white);border-radius:3px;display:flex;align-items:center;gap:8px;padding-left:14px;color:var(--white)}
.call small{display:block;font-size:10px;opacity:.85}
.call b{display:block;font-size:14px;font-weight:500}
.dots span{display:block;width:12px;height:12px;border:1.5px solid #555;border-radius:50%;margin-bottom:9px;background:var(--white)}
.dots span.on{background:var(--lime);border-color:var(--lime)}
.scroll{left:558px;top:646px;width:72px;height:72px;border-radius:50%;background:var(--white);border:3px solid var(--green);
  display:flex;flex-direction:column;align-items:center;justify-content:center;font-size:9px;font-weight:600;color:var(--ink);line-height:10px;text-align:center}

/* SECTION HEADS */
.eyebrow{font-size:13px;text-transform:uppercase;color:var(--ink)}
.sec-title{font-size:46px;line-height:46px}
.rule{height:4px;background:var(--green)}

/* ABOUT */
.about-copy{left:113px;width:470px;font-size:14px;line-height:25px;color:var(--text)}
.about-gold{left:609px;top:864px;width:162px;height:127px;background:var(--gold)}
.about-photo{left:626px;top:881px;width:508px;height:454px;background:linear-gradient(180deg,#4f8fd6 0%,#a9cdee 40%,#b78552 60%,#3c3f44 85%,#6d6f72 100%)}

/* SERVICES */
.svc-gold{left:0;top:1475px;width:1200px;height:940px;background:var(--gold);
  clip-path:polygon(0 0,100% 0,100% 790px,50% 930px,0 790px)}
.svc-bg{left:0;top:1475px;width:1200px;height:930px;background:linear-gradient(180deg,#1a9a3c 0%,#17883a 60%,#1a9a3c 100%);
  clip-path:polygon(0 0,100% 0,100% 778px,50% 918px,0 778px)}
.white{color:var(--white)}
.tile{width:354px;height:354px}
.tile svg.shape{position:absolute;left:0;top:0}
.tile .in{position:absolute;left:62px;top:44px;width:230px;text-align:center}
.tile .ico{width:88px;height:88px;border-radius:50%;background:var(--green);margin:0 auto 12px;display:flex;align-items:center;justify-content:center}
.tile h3{font-size:19px;font-weight:500;color:var(--ink);margin-bottom:6px}
.tile p{font-size:12px;line-height:20px;color:#333}
.tile .more{display:inline-block;margin-top:8px;font-size:12px;text-decoration:underline;color:#333}
.tile.feature h3,.tile.feature p,.tile.feature .more{color:var(--white)}

/* PROJECTS */
.proj{overflow:hidden}
.proj .ph{position:absolute;inset:0}
.proj .tag{position:absolute;left:0;right:0;bottom:0;height:27px;background:var(--green);color:var(--white);font-size:13px;font-weight:500;padding:6px 12px;text-transform:uppercase}
.proj-feature .ph{background:linear-gradient(160deg,#4a3a30 0%,#6a3f27 55%,#4a2a1a 100%)}
.proj-feature .frame{position:absolute;left:10px;top:10px;right:10px;bottom:10px;border:2px dashed var(--lime)}
.proj-feature .cap{position:absolute;left:0;right:0;top:95px;text-align:center;color:var(--white);font-size:15px;line-height:25px;padding:0 20px}
.proj-feature .cap b{display:block;color:var(--lime);font-size:21px;font-weight:600;margin-bottom:10px}

/* CONTACT */
.contact-copy{left:116px;top:3464px;width:400px;font-size:16px;line-height:26px;color:#333}
.ci{left:113px;display:flex;align-items:center;gap:20px}
.ci .c{width:38px;height:38px;border-radius:50%;background:var(--green);display:flex;align-items:center;justify-content:center;flex:none}
.ci small{display:block;font-size:13px;color:#444}
.ci b{display:block;font-size:15px;font-weight:600;color:var(--ink)}
.field{left:577px;width:512px;background:var(--field);color:#ddd;font-size:13px;padding:12px 18px;border-radius:2px}
.worker{left:1000px;top:3560px;width:200px;height:330px;background:linear-gradient(160deg,rgba(255,255,255,0) 0%,#f2b06a 40%,#d64f8c 70%,#3a5bd2 100%)}

/* FOOTER */
.skyline{left:0;top:3890px;width:1200px;height:60px;background:var(--black)}
.footer{left:0;top:3950px;width:1200px;height:341px;background:var(--black)}
.foot-logo{left:265px;top:4023px;width:127px;height:143px;display:flex;align-items:center;justify-content:center;font-family:"Bebas Neue",sans-serif;font-size:30px;color:var(--white);text-align:center;line-height:1}
.social{top:4196px;width:38px;height:38px;border-radius:50%;border:1.5px solid var(--gold)}
.social.on{background:var(--green);border-color:var(--green)}
.fcol h4{font-size:20px;font-weight:500;color:var(--white)}
.fcol .u{width:50px;height:3px;background:var(--green);margin:8px 0 18px}
.fcol a{display:block;font-size:13px;color:#ddd;line-height:26px}
.bottom{left:0;top:4291px;width:1200px;height:57px;background:#5a4a2a;color:var(--white);font-size:14px;text-align:center;line-height:57px}
.totop{left:1116px;top:4267px;width:39px;height:39px;background:var(--green);border-radius:4px;display:flex;align-items:center;justify-content:center}
</style>
</head>
<body>

<!-- HERO -->
<div class="abs hero-gold"></div>
<div class="abs hero-photo" role="img" aria-label="Builder working on a timber roof frame against a blue sky"></div>
<div class="abs logo">MARROWVALE</div>
<nav class="abs nav">
  <a class="active" href="#">Home</a><a href="#">Services</a><a href="#">About Us</a><a href="#">Our Projects</a>
</nav>
<a class="abs btn btn-lime" style="left:820px;top:27px;width:203px;height:44px">Request a Free Quote</a>
<a class="abs btn btn-green" style="left:1040px;top:27px;width:125px;height:44px">Contact Us</a>
<h1 class="abs display hero-title" style="top:153px"><span class="hl">Crafting Quality</span> Homes and Spaces</h1>
<div class="abs display hero-title" style="top:226px">With Excellence</div>
<p class="abs hero-sub">We specialize in building, landscaping, decking, and more<br>to bring your vision to life.</p>
<div class="abs call btn-green" style="left:451px"><svg width="16" height="16" viewBox="0 0 24 24"><path fill="#fff" d="M6.6 10.8a15 15 0 006.6 6.6l2.2-2.2c.3-.3.7-.4 1-.2 1.1.4 2.3.6 3.6.6.6 0 1 .4 1 1V20c0 .6-.4 1-1 1A17 17 0 013 4c0-.6.4-1 1-1h3.5c.6 0 1 .4 1 1 0 1.3.2 2.5.6 3.6.1.3 0 .7-.2 1z"/></svg><div><small>DANIEL</small><b>0400 123 456</b></div></div>
<div class="abs call btn-lime" style="left:604px"><svg width="16" height="16" viewBox="0 0 24 24"><path fill="#fff" d="M6.6 10.8a15 15 0 006.6 6.6l2.2-2.2c.3-.3.7-.4 1-.2 1.1.4 2.3.6 3.6.6.6 0 1 .4 1 1V20c0 .6-.4 1-1 1A17 17 0 013 4c0-.6.4-1 1-1h3.5c.6 0 1 .4 1 1 0 1.3.2 2.5.6 3.6.1.3 0 .7-.2 1z"/></svg><div><small>PRIYA</small><b>0400 987 654</b></div></div>
<div class="abs dots" style="left:51px;top:337px"><span></span><span class="on"></span><span></span><span></span></div>
<div class="abs scroll">SCROLL<br>DOWN<svg width="12" height="16" viewBox="0 0 12 16" style="margin-top:3px"><path d="M6 1v13M1 9l5 5 5-5" stroke="#9a7b4a" stroke-width="1.5" fill="none"/></svg></div>

<!-- ABOUT -->
<div class="abs eyebrow" style="left:113px;top:858px">Who we are</div>
<h2 class="abs display sec-title" style="left:113px;top:880px">About Us</h2>
<div class="abs rule" style="left:113px;top:939px;width:125px"></div>
<p class="abs about-copy" style="top:963px">We have a wealth of knowledge and experience in the landscaping and construction industries. we offer creative solutions for every DREAM &amp; ANY budget.</p>
<p class="abs about-copy" style="top:1048px">Saerspiciatis undeasepoiise oklasdo mnis aidaste natus error siset voluptatem accusan tium doloremque laudantium, totam reseem aperiam, ease aque ipaefdsa quae ab illo inventore veritatis essease quasi architecto beatae vitae dicta sunt explicabo. Nemo esenseim ipsam voluptatem quia volasdfupta sde sessitasese aspersenseatur autodit aut fugitsdsed quisaea consequuntur magni dolores seeos qui ratione voluptatem sequi nesciunt.</p>
<a class="abs btn btn-green" style="left:113px;top:1252px;width:127px;height:45px">Learn More</a>
<div class="abs about-gold"></div>
<div class="abs about-photo" role="img" aria-label="Modern timber-clad building with large glass windows"></div>
<svg class="abs" style="left:900px;top:1200px" width="270" height="190" aria-hidden="true">
  <defs><pattern id="dotgrid" width="14" height="14" patternUnits="userSpaceOnUse"><circle cx="3" cy="3" r="1.6" fill="#555"/></pattern></defs>
  <rect x="0" y="140" width="270" height="50" fill="url(#dotgrid)"/>
  <rect x="234" y="0" width="36" height="190" fill="url(#dotgrid)"/>
</svg>

<!-- SERVICES -->
<div class="abs svc-gold"></div>
<div class="abs svc-bg" role="img" aria-label="Green-tinted photo of a house exterior"></div>
<div class="abs eyebrow white" style="left:0;width:1200px;text-align:center;top:1575px">What we do</div>
<h2 class="abs display sec-title white" style="left:0;width:1200px;text-align:center;top:1596px">Our Services</h2>
<div class="abs rule" style="left:537px;top:1656px;width:126px;background:var(--white)"></div>

<div class="abs tile" style="left:51px;top:1686px">
  <svg class="shape" width="354" height="354"><polygon points="177,0 354,177 177,354 0,177" fill="#fff"/><circle cx="24" cy="177" r="6" fill="#222"/><circle cx="330" cy="177" r="6" fill="#222"/></svg>
  <div class="in"><div class="ico"><svg width="44" height="44" viewBox="0 0 24 24" fill="none" stroke="#fff" stroke-width="1.3"><rect x="5" y="4" width="14" height="17"/><path d="M8 7h2M12 7h2M8 11h2M12 11h2M8 15h2M12 15h2M10 21v-3h4v3"/></svg></div>
  <h3>BUILDING</h3><p>Gaerspiciatis unde omnis iste natus error sit voluptatem accusantium doloremque laudantium aeapiciatis unde omsea assesenis.</p><a class="more">LEARN MORE</a></div>
</div>
<div class="abs tile" style="left:419px;top:1686px">
  <svg class="shape" width="354" height="354"><polygon points="177,0 354,177 177,354 0,177" fill="#fff"/><circle cx="24" cy="177" r="6" fill="#222"/><circle cx="330" cy="177" r="6" fill="#222"/></svg>
  <div class="in"><div class="ico"><svg width="44" height="44" viewBox="0 0 24 24" fill="none" stroke="#fff" stroke-width="1.3"><path d="M7 20V10M7 10c-3 0-3-6 0-7 3 1 3 7 0 7zM12 20V8M17 20v-8M3 20h18"/></svg></div>
  <h3>LANDSCAPING</h3><p>Gaerspiciatis unde omnis iste natus error sit voluptatem accusantium doloremque laudantium aeapiciatis unde omsea assesenis.</p><a class="more">LEARN MORE</a></div>
</div>
<div class="abs tile" style="left:788px;top:1686px">
  <svg class="shape" width="354" height="354"><polygon points="177,0 354,177 177,354 0,177" fill="#fff"/><circle cx="24" cy="177" r="6" fill="#222"/><circle cx="330" cy="177" r="6" fill="#222"/></svg>
  <div class="in"><div class="ico"><svg width="44" height="44" viewBox="0 0 24 24" fill="none" stroke="#fff" stroke-width="1.3"><rect x="4" y="4" width="16" height="16"/><path d="M4 8h16M4 12h16M4 16h16"/></svg></div>
  <h3>DECKING</h3><p>Gaerspiciatis unde omnis iste natus error sit voluptatem accusantium doloremque laudantium aeapiciatis unde omsea assesenis.</p><a class="more">LEARN MORE</a></div>
</div>
<div class="abs tile" style="left:235px;top:1896px">
  <svg class="shape" width="354" height="354"><polygon points="177,0 354,177 177,354 0,177" fill="#fff"/><circle cx="24" cy="177" r="6" fill="#222"/><circle cx="330" cy="177" r="6" fill="#222"/></svg>
  <div class="in"><div class="ico"><svg width="44" height="44" viewBox="0 0 24 24" fill="none" stroke="#fff" stroke-width="1.3"><circle cx="15" cy="8" r="4"/><path d="M12 11l-7 7 2 2 7-7M6 4l3 3"/></svg></div>
  <h3>MAINTENANCE</h3><p>Gaerspiciatis unde omnis iste natus error sit voluptatem accusantium doloremque laudantium aeapiciatis unde omsea assesenis.</p><a class="more">LEARN MORE</a></div>
</div>
<div class="abs tile feature" style="left:603px;top:1896px">
  <svg class="shape" width="354" height="354"><polygon points="177,0 354,177 177,354 0,177" fill="#9a7b4a" fill-opacity=".92"/><circle cx="24" cy="177" r="6" fill="#222"/><circle cx="330" cy="177" r="6" fill="#222"/></svg>
  <div class="in"><div class="ico"><svg width="44" height="44" viewBox="0 0 24 24" fill="none" stroke="#fff" stroke-width="1.3"><path d="M3 18L10 6h8l3 12zM7 12h12M5 15h15M13 6l-4 12M17 6l-3 12"/></svg></div>
  <h3>ROOFING</h3><p>Gaerspiciatis unde omnis iste natus error sit voluptatem accusantium doloremque laudantium aeapiciatis unde omsea assesenis.</p><a class="more">LEARN MORE</a></div>
</div>
<a class="abs btn btn-gold" style="left:537px;top:2194px;width:126px;height:46px;border:1px solid #fff">Learn More</a>

<!-- PROJECTS -->
<div class="abs eyebrow" style="left:0;width:1200px;text-align:center;top:2489px">Portfolio</div>
<h2 class="abs display sec-title" style="left:0;width:1200px;text-align:center;top:2510px">Our Projects</h2>
<div class="abs rule" style="left:537px;top:2570px;width:126px"></div>

<div class="abs proj proj-feature" style="left:113px;top:2620px;width:484px;height:268px">
  <div class="ph" role="img" aria-label="Timber deck at dusk"></div><div class="frame"></div>
  <div class="cap"><b>DECKING</b>Gaerspiciatis unde omnis iste natus error sit voluptatem accusantium doloremque laudantium.</div>
</div>
<div class="abs proj" style="left:603px;top:2620px;width:239px;height:268px"><div class="ph" role="img" aria-label="Glass office building at sunset" style="background:linear-gradient(180deg,#e0a066,#6d86b5 40%,#2f3d5a 80%,#444)"></div><div class="tag">Building</div></div>
<div class="abs proj" style="left:846px;top:2620px;width:241px;height:268px"><div class="ph" role="img" aria-label="Brick home with green lawn" style="background:linear-gradient(180deg,#b9d3ea,#b48866 35%,#6a9a3a 60%,#7fb043)"></div><div class="tag">Landscaping</div></div>
<div class="abs proj" style="left:113px;top:2893px;width:240px;height:269px"><div class="ph" role="img" aria-label="Timber deck in a backyard" style="background:linear-gradient(180deg,#b7c6d8,#8a7f76 35%,#8a3f22 65%,#6b2e18)"></div><div class="tag">Maintenance</div></div>
<div class="abs proj" style="left:358px;top:2893px;width:239px;height:269px"><div class="ph" role="img" aria-label="House with grey shingle roof" style="background:linear-gradient(180deg,#c9d8ea,#6b6f75 45%,#d8d4cc 80%,#8a8a80)"></div><div class="tag">Roofing</div></div>
<div class="abs proj" style="left:603px;top:2893px;width:484px;height:269px"><div class="ph" role="img" aria-label="Two steel carport structures" style="background:linear-gradient(180deg,#e8e8e8,#5a5a58 30%,#8a8a80 60%,#a08a6a)"></div><div class="tag">Gutters</div></div>

<a class="abs btn btn-lime" style="left:429px;top:3211px;width:152px;height:47px;border-radius:3px 0 0 3px">View All</a>
<a class="abs btn btn-green" style="left:581px;top:3211px;width:155px;height:47px;border-radius:0 3px 3px 0;padding-left:22px">Contact Us</a>
<div class="abs" style="left:566px;top:3221px;width:28px;height:28px;border-radius:50%;border:1.5px solid #fff;background:var(--gold)"></div>

<!-- CONTACT -->
<div class="abs eyebrow" style="left:116px;top:3351px">Get in touch</div>
<h2 class="abs display sec-title" style="left:116px;top:3372px">Contact Us</h2>
<div class="abs rule" style="left:116px;top:3431px;width:125px"></div>
<p class="abs contact-copy">Perspiciatis unde omnis iste natus error ssadsdit voluptatem accusantium doloremque laudanti umtotam rem aperiam, eaque ipsa quventore.</p>
<div class="abs ci" style="top:3566px"><div class="c"><svg width="18" height="18" viewBox="0 0 24 24"><path fill="#fff" d="M6.6 10.8a15 15 0 006.6 6.6l2.2-2.2c.3-.3.7-.4 1-.2 1.1.4 2.3.6 3.6.6.6 0 1 .4 1 1V20c0 .6-.4 1-1 1A17 17 0 013 4c0-.6.4-1 1-1h3.5c.6 0 1 .4 1 1 0 1.3.2 2.5.6 3.6.1.3 0 .7-.2 1z"/></svg></div>
  <div><small>DANIEL</small><b>0400 123 456</b></div><div style="width:1px;height:34px;background:#999"></div><div><small>PRIYA</small><b>0400 987 654</b></div></div>
<div class="abs ci" style="top:3635px"><div class="c"><svg width="18" height="18" viewBox="0 0 24 24" fill="none" stroke="#fff" stroke-width="1.8"><rect x="3" y="6" width="18" height="12"/><path d="M3 6l9 7 9-7"/></svg></div><div><small>Email</small><b>info@marrowvalehomes.example</b></div></div>
<div class="abs ci" style="top:3704px"><div class="c"><svg width="18" height="18" viewBox="0 0 24 24"><path fill="#fff" d="M12 2a7 7 0 00-7 7c0 5 7 13 7 13s7-8 7-13a7 7 0 00-7-7zm0 9.5A2.5 2.5 0 1112 6a2.5 2.5 0 010 5.5z"/></svg></div><div><small>Address</small><b>128 Willow Crescent, Springfield, CA 90000</b></div></div>

<div class="abs worker" role="img" aria-label="Colourful illustration of a construction worker"></div>
<div class="abs field" style="top:3403px;height:41px">Your Name</div>
<div class="abs field" style="top:3464px;height:40px">Email</div>
<div class="abs field" style="top:3523px;height:40px">Phone Number</div>
<div class="abs field" style="top:3582px;height:125px">Enter Your Message</div>
<a class="abs btn btn-green" style="left:577px;top:3726px;width:154px;height:43px">Contact Us</a>

<!-- FOOTER -->
<div class="abs skyline" role="img" aria-label="Dark silhouette of a row of houses"></div>
<div class="abs footer"></div>
<div class="abs foot-logo">MARROWVALE</div>
<div class="abs social" style="left:251px" aria-label="Social profile"></div>
<div class="abs social on" style="left:305px" aria-label="Social profile"></div>
<div class="abs social" style="left:359px" aria-label="Social profile"></div>
<div class="abs fcol" style="left:515px;top:4038px"><h4>Quick Links</h4><div class="u"></div><a>Home</a><a>Services</a><a>Portfolio</a><a>About Us</a><a>Contact Us</a></div>
<div class="abs fcol" style="left:726px;top:4038px"><h4>Links</h4><div class="u"></div><a>Copyright</a><a>Legal</a><a>Privacy</a><a>Accessibility</a><a>Sitemap</a></div>
<div class="abs fcol" style="left:903px;top:4038px"><h4>Support</h4><div class="u"></div><a>Team</a><a>About Us</a><a>Careers</a><a>Our Values</a></div>
<div class="abs bottom">©2024. All rights reserved.</div>
<div class="abs totop"><svg width="16" height="16" viewBox="0 0 16 16"><path d="M3 10l5-5 5 5" stroke="#fff" stroke-width="2" fill="none"/></svg></div>

</body>
</html>
```